The Gentle Moonlit Harbour Journey

This book accompanies a video workshop. The book explains who our guardian angels are, what is their purpose, how to connect with them for wisdom & guidance. How to manifest what we world like bring into our lives by asking the Angels. The book contains meditation exercises, lots of information and fun facts about how our angels give us messages and guidance and how to become more intuitive. How to use angel oracle cards to receive guidance from our angels.
I'm quite an upbeat, happy person, so the book is written very warmly and is a collection of all the information that out ther, drawn together neatly by me, with my own unique take on all things angelic. Along with personal stories and anecdotes about how and why I became interested in angels and what they have taught me. It's fun, fresh, lighthearted and modern. Not at all serious, just extremely uplifting and positive, so I would really like the cover to reflect this.

Target Market(s)

Anyone who is interested in angels. From my chatterloop page activity I find it is mostly women of all ages who are interested in angels

Font styles to use
Serif
Sans Serif
Script

Colors
ea8dbb
f04a50
e667a6
e34197
85abd2
886aae
b7a5cd
6b449b
fbee3e

Requirements
Must have
• A more feminine appeal
• Look quite modern & upbeat but also calming and open
• I would like it to look etherel in some way. I definitely dont want something that looks like a cartoon or clip art
Should not have
• No dark colours or sinister imagery. I don't want people to feel like thus can't do the & it's only special people who can connect with their angels
• No haunting imagery!

```html
<!DOCTYPE html>
<html lang="en">
<head>
<meta charset="utf-8">
<title>The Gentle Moonlit Harbour Journey – Book Cover</title>
<link rel="stylesheet" href="https://fonts.googleapis.com/css2?family=Cormorant+Garamond:ital,wght@0,400;1,400&family=EB+Garamond:wght@400&family=Great+Vibes&display=swap">
<style>
  :root {
    --page-bg: #ffffff;
    --sky-top: #5a2f82;
    --sky-violet: #7a3f95;
    --sky-magenta: #b2559f;
    --sky-pink: #d985b6;
    --cloud-lilac: #c6a3d0;
    --cloud-deep: #8a5fa8;
    --ink-light: #ffffff;
    --text-shadow: rgba(70, 20, 90, 0.45);
  }
  * { margin: 0; padding: 0; box-sizing: border-box; }
  html, body {
    width: 1200px;
    height: 1000px;
    overflow: hidden;
    background: var(--page-bg);
  }
  .canvas {
    position: relative;
    width: 1200px;
    height: 1000px;
  }
  .book-cover {
    position: absolute;
    left: 293px;
    top: 93px;
    width: 609px;
    height: 787px;
    overflow: hidden;
    color: var(--ink-light);
    text-align: center;
  }
  .cover-art {
    position: absolute;
    inset: 0;
    width: 100%;
    height: 100%;
  }
  .tagline {
    position: absolute;
    top: 26px;
    left: 0;
    right: 0;
    font-family: "Cormorant Garamond", Georgia, serif;
    font-style: italic;
    font-size: 20px;
    line-height: 26px;
    letter-spacing: 0.3px;
    text-shadow: 0 1px 4px var(--text-shadow);
  }
  .title {
    position: absolute;
    top: 270px;
    left: 0;
    right: 0;
    font-weight: 400;
    text-shadow: 0 2px 8px var(--text-shadow);
  }
  .title-lead {
    display: block;
    font-family: "EB Garamond", Georgia, serif;
    font-size: 36px;
    line-height: 40px;
    padding-left: 160px;
  }
  .title-script {
    display: block;
    font-family: "Great Vibes", cursive;
    font-size: 104px;
    line-height: 104px;
    margin-top: 4px;
  }
  .title-tail {
    display: block;
    font-family: "EB Garamond", Georgia, serif;
    font-size: 38px;
    line-height: 42px;
    margin-top: 4px;
  }
  .author {
    position: absolute;
    bottom: 22px;
    left: 0;
    right: 0;
    font-family: "EB Garamond", Georgia, serif;
    font-size: 38px;
    letter-spacing: 0.5px;
    text-shadow: 0 1px 6px var(--text-shadow);
  }
</style>
</head>
<body>
<main class="canvas">
  <section class="book-cover">
    <svg class="cover-art" viewBox="0 0 609 787" preserveAspectRatio="none" role="img" aria-label="Ethereal photograph of a winged angel shape formed by pink clouds in a violet sky above a sea of clouds">
      <defs>
        <linearGradient id="sky" x1="0" y1="0" x2="0" y2="1">
          <stop offset="0" stop-color="var(--sky-top)"/>
          <stop offset="0.35" stop-color="var(--sky-violet)"/>
          <stop offset="0.62" stop-color="var(--sky-magenta)"/>
          <stop offset="0.76" stop-color="var(--sky-pink)"/>
          <stop offset="0.84" stop-color="var(--cloud-lilac)"/>
          <stop offset="1" stop-color="var(--cloud-deep)"/>
        </linearGradient>
        <radialGradient id="glow" cx="0.45" cy="0.36" r="0.45">
          <stop offset="0" stop-color="#f3c6e0" stop-opacity="0.75"/>
          <stop offset="1" stop-color="#f3c6e0" stop-opacity="0"/>
        </radialGradient>
      </defs>
      <rect width="609" height="787" fill="url(#sky)"/>
      <rect width="609" height="787" fill="url(#glow)"/>
    </svg>

    <p class="tagline">Connect with your angels,<br>bring love, healing and divine guidance<br>to every area of your life</p>

    <h1 class="title">
      <span class="title-lead">The gentle</span>
      <span class="title-script">Moonlit Harbour</span>
      <span class="title-tail">journey</span>
    </h1>

    <p class="author">Rosalind Marche</p>
  </section>
</main>
</body>
</html>
```